Etikett für Honigunternehmen gesucht
Zielgruppe
Wir produzieren Honig, möchten aber in naher Zukunft auch andere Honigprodukte produzieren (Cremen, Wein, Likör......). Unsere Zielgruppe sind alle.
Aufgabenstellung
Wir wünschen uns Schlichtheit und Einfachheit. Wichtig ist uns auch, dass das Design modern wirkt. Es soll kein typisches Honigetikett mit 'Wiesen und Bienen' werden. Das Glas wird auch schlicht und modern werden. Es wird nur 250-g- und 500-g-Gläser geben. Die Gewichtsangabe muss sichtbar und mind. 4 mm groß sein. Name, Anschrift und Telefonnummer können auch am Deckel oder ganz klein und leserlich am unteren Etikettenrand stehen. Dabei ist zu beachten, dass der kleinste Buchstabe min. 1,2 mm groß ist.
Etiketten-Design für Honigglas Etiketten-Design für Honigglas"
Format: Etikett für 250-gr.-Honigglas (TO ∅ 63 mm). Standardmaßgrösse 165 × 40 mm Design: schlicht, hochwertig, modern, edel/royal, unkonventionelles Design (weg von Bienen, Waben, Landschaften usw.), dunkle Farbtöne in Kontrast zu heller Schrift, die beiden Textbausteine 'Los Nr. ' sowi..
Attraktives Etiketten-Design für Honig Attraktives Etiketten-Design für Honig"
Wir verkaufen zur Zeit vor allem Waldhonig, streben aber auch einen Blütenhonig an. Das Etikett soll daher entweder den Wald wiederspiegeln oder aber neutral sein, so dass der Schriftzug Waldhonig oder Blütenhonig jeweils eingesetzt werden kann. Wichtig ist mir der Ortszusatz 'aus dem Glottertal..
Etiketten-Design für Produkte eines Familienbetriebs mit Imkerei und Hühnerhaltung Etiketten-Design für Produkte eines Familienbetriebs mit Imkerei und Hühnerhaltung"
1. Zentrale, auf allen Etiketten wiederkehrende Elemente: - Unser Riegelhaus (stilisiert) (Bild beiliegend) - Das Wort 'Marlock' (Anmerkung: ohne Anführungszeichen) - die zentralen Elemente sollen die Produkte nicht überragen. 2. Dezente Adresse: - Familie Obrecht, Talbrunn, CH-9388 Forlenz 3...
Etiketten-Design für Kurkuma-Honig Etiketten-Design für Kurkuma-Honig"
Etikett für 500g // Stanze eckig (210x35mm), Druckdatei entsprechend Vorgaben https://etikettwerk-muster.de/faq/ Vorgaben für das Grünquell Logo im Anhang Vorgaben für EG Öko Logo : https://example-oekoamt.eu/landbau/bio/download/logo_de Pflichtangaben auf dem Etikett: Gewicht, Adresse siehe Beispiel..
Etiketten-Design für Blütenhonig und Waldhonig gesucht Etiketten-Design für Blütenhonig und Waldhonig gesucht"
Zwei verschiedene Etiketten-Desings 1 x Blütenhonig sowie 1 x Waldhonig für unterschiedliche Honigglasgrößen (500 g und 250 g) Die Maße für die Etiketten wären: Für 500-Gramm-Glas 210 mm x 45 mm für's 250-Gramm-Glas 180 mm x 38 mm. Wir sind auch offen für neue Vorschläge bezüglich ..

```html
<!DOCTYPE html>
<html lang="de">
<head>
<meta charset="utf-8">
<title>Sonnwald Imkerei – Blütenhonig Etikett</title>
<link rel="stylesheet" href="https://fonts.googleapis.com/css2?family=Caveat:wght@400&family=Quicksand:wght@300;400&display=swap">
<style>
  :root {
    --backdrop: #fdecc6;
    --label-white: #fbfbfa;
    --honey: #f2a71c;
    --band-light: #f6b46a;
    --band-dark: #ee9a3a;
  }
  * { margin: 0; padding: 0; box-sizing: border-box; }
  html, body {
    width: 1200px;
    height: 849px;
    overflow: hidden;
    background: var(--backdrop);
  }
  .canvas {
    width: 1200px;
    height: 849px;
    display: flex;
    align-items: center;
    justify-content: center;
  }
  .label {
    width: 680px;
    height: 576px;
    display: flex;
    flex-direction: column;
    box-shadow: 0 10px 30px rgba(180, 120, 40, 0.15);
  }
  .label__main {
    flex: 0 0 409px;
    background: var(--label-white);
    display: flex;
    flex-direction: column;
    align-items: center;
    padding-top: 52px;
    color: var(--honey);
  }
  .brand {
    font-family: 'Quicksand', sans-serif;
    font-weight: 300;
    font-size: 54px;
    line-height: 1;
    letter-spacing: 1px;
    color: var(--honey);
    display: flex;
    align-items: center;
    gap: 18px;
  }
  .brand__dot {
    width: 26px;
    height: 26px;
    border-radius: 50%;
    background: var(--honey);
  }
  .product-name {
    font-family: 'Caveat', cursive;
    font-weight: 400;
    font-size: 68px;
    line-height: 1;
    margin-top: 62px;
  }
  .net-weight {
    font-family: 'Caveat', cursive;
    font-size: 34px;
    line-height: 1;
    margin-top: 6px;
  }
  .producer {
    font-family: 'Quicksand', sans-serif;
    font-weight: 400;
    font-style: normal;
    font-size: 12px;
    line-height: 1.4;
    margin-top: 26px;
    text-align: center;
  }
  .producer__sep { margin: 0 6px; }
  .label__band {
    flex: 1;
    background: linear-gradient(180deg, var(--band-light) 0%, var(--band-dark) 100%);
  }
</style>
</head>
<body>
  <main class="canvas">
    <section class="label">
      <div class="label__main">
        <h1 class="brand">Sonnwald Imkerei <span class="brand__dot"></span></h1>
        <p class="product-name">Blütenhonig</p>
        <p class="net-weight">500g</p>
        <address class="producer">
          Valentin Moserhuber<span class="producer__sep">|</span>Am Lerchenhang 14<span class="producer__sep">|</span>4283 Wiesenried<br>
          Herkunftsland Österreich<span class="producer__sep">|</span>Tel.: +43 660 5172 0394
        </address>
      </div>
      <div class="label__band" role="img" aria-label="Dekoratives Muster aus kleinen gekrönten Bienen auf orangem Grund"></div>
    </section>
  </main>
</body>
</html>
```